Feature Nomination Banner

Create a 600 x 160 banner advertisement for Counsel and Bench Review’s feature story nominations. We’ve included the Counsel and Bench Review logo (black and white versions) for inclusion.
Headline: Now Accepting Nominations for 2024 Features
Nominate an Outstanding Lawyer or Law Firm Today!

```html
<!DOCTYPE html>
<html lang="en">
<head>
<meta charset="utf-8">
<title>Feature Nomination Banner</title>
<link rel="stylesheet" href="https://fonts.googleapis.com/css2?family=Montserrat:wght@500;700&family=Mulish:wght@500&display=swap">
<style>
  :root {
    --page: #ffffff;
    --indigo: #3b3a6f;
    --gold: #b39b5f;
    --ink: #111111;
    --white: #ffffff;
    --photo-dark: #2e2620;
    --photo-mid: #5a4a3e;
    --photo-light: #8a7c70;
  }
  * { margin: 0; padding: 0; box-sizing: border-box; }
  html, body {
    width: 1200px;
    height: 1050px;
    overflow: hidden;
    background: var(--page);
  }
  .banner {
    position: absolute;
    left: 0;
    top: 365px;
    width: 1200px;
    height: 320px;
    background: var(--indigo);
    overflow: hidden;
  }
  .banner__photo {
    position: absolute;
    inset: 0;
  }
  .banner__brand {
    position: absolute;
    left: 0;
    width: 760px;
    top: 34px;
    text-align: center;
    font-family: "Montserrat", sans-serif;
    font-weight: 500;
    font-size: 30px;
    letter-spacing: 1px;
    color: var(--white);
    text-transform: uppercase;
  }
  .banner__headline {
    position: absolute;
    left: 0;
    width: 770px;
    top: 130px;
    text-align: center;
    font-family: "Montserrat", sans-serif;
    font-weight: 700;
    font-size: 40px;
    line-height: 44px;
    color: var(--white);
    text-transform: uppercase;
  }
  .banner__cta {
    position: absolute;
    left: 0;
    top: 250px;
    width: 900px;
    height: 70px;
    background: var(--gold);
    font-family: "Mulish", sans-serif;
    font-weight: 500;
    font-size: 31px;
    line-height: 70px;
    padding-left: 40px;
    color: var(--ink);
  }
  .banner__corner {
    position: absolute;
    left: 868px;
    top: 250px;
  }
</style>
</head>
<body>
  <section class="banner">
    <svg class="banner__photo" width="1200" height="320" viewBox="0 0 1200 320">
      <defs>
        <linearGradient id="office-tones" x1="0" y1="0" x2="1" y2="1">
          <stop offset="0" stop-color="var(--photo-mid)"/>
          <stop offset="0.5" stop-color="var(--photo-dark)"/>
          <stop offset="1" stop-color="var(--photo-light)"/>
        </linearGradient>
      </defs>
      <path role="img" aria-label="Group photo of lawyers standing in a law office library"
            d="M 850 0 L 1200 0 L 1200 320 L 780 320 C 740 250 730 110 850 0 Z"
            fill="url(#office-tones)"/>
      <path d="M 850 0 C 730 110 740 250 780 320" fill="none" stroke="var(--white)" stroke-width="6"/>
    </svg>
    <div class="banner__brand">Counsel and Bench Review</div>
    <h1 class="banner__headline">Now Accepting Nominations<br>for 2024 Features</h1>
    <p class="banner__cta">Nominate an Outstanding Lawyer or Law Firm Today!</p>
    <svg class="banner__corner" width="32" height="32" viewBox="0 0 32 32">
      <path d="M 4 4 L 28 4 L 28 28" fill="none" stroke="var(--white)" stroke-width="6"/>
    </svg>
  </section>
</body>
</html>
```